halbrook paving works

Needs to have phone number 0418352790 and email carlwhitby@mailnest.com.au.
ABN 27813046652
name carl whitby

For all your concreting solutions
Excavation
Exposed & colour concrete
House & shed slabs
Driveways
Landing & steps

Contact Information for Business Card

ph 0418352790
email carlwhitby@mailnest.com.au.
ABN 27813046652
name carl whitby

```html
<!DOCTYPE html>
<html lang="en">
<head>
<meta charset="utf-8">
<title>Halbrook Paving Works – Business Card</title>
<link rel="stylesheet" href="https://fonts.googleapis.com/css2?family=Montserrat:wght@600;700&family=Open+Sans:wght@400;600&display=swap">
<style>
  :root {
    --orange: #f26a22;
    --orange-light: #f47f3e;
    --charcoal: #4a4a4a;
    --grey: #5f5f5f;
    --ink: #2b2b2b;
    --paper: #ffffff;
    --backdrop: #e6e6e6;
  }
  * { box-sizing: border-box; margin: 0; padding: 0; }
  html, body {
    width: 1200px; height: 782px; overflow: hidden;
    background: var(--backdrop);
  }
  .canvas {
    position: relative; width: 1200px; height: 782px;
    display: flex; align-items: center; justify-content: center; gap: 40px;
  }
  .card {
    position: relative; width: 540px; height: 309px; overflow: hidden;
    box-shadow: 0 6px 18px rgba(0,0,0,.18);
  }

  /* Front */
  .card--front { background: var(--paper); font-family: "Open Sans", sans-serif; color: var(--ink); }
  .holder {
    position: absolute; left: 26px; top: 20px;
    font-family: "Montserrat", sans-serif; font-weight: 700; font-size: 16px; letter-spacing: .3px;
    color: var(--grey);
  }
  .holder__first { color: var(--orange); }
  .brand {
    position: absolute; left: 26px; top: 86px; display: flex; align-items: center; gap: 14px;
  }
  .brand__square { width: 44px; height: 44px; background: var(--orange); }
  .brand__rule { width: 2px; height: 70px; background: var(--orange); }
  .brand__name {
    font-family: "Montserrat", sans-serif; font-weight: 700; font-size: 17px; line-height: 1.2;
    color: var(--orange); letter-spacing: .4px; text-transform: uppercase;
  }
  .abn {
    position: absolute; right: 26px; top: 128px;
    font-size: 12px; font-weight: 600; letter-spacing: .4px; color: var(--ink);
  }
  .contact { position: absolute; left: 26px; top: 198px; list-style: none; font-size: 12px; line-height: 1.55; }
  .contact li { display: flex; align-items: center; gap: 7px; }
  .contact svg { width: 11px; height: 11px; flex: none; }
  .services {
    position: absolute; right: 26px; top: 176px; list-style: none; text-align: right;
    font-size: 12.5px; line-height: 1.35;
  }
  .services__lead {
    font-family: "Montserrat", sans-serif; font-weight: 600; font-size: 10px; line-height: 1.25;
    color: var(--orange); text-transform: uppercase; margin-bottom: 3px;
  }
  .services li { display: flex; justify-content: flex-end; align-items: center; gap: 5px; }
  .services li::after { content: ""; width: 8px; height: 8px; background: var(--orange); flex: none; }
  .services li.services__lead::after { display: none; }
  .footer-bands { position: absolute; left: 0; bottom: 0; width: 540px; height: 34px; }

  /* Back */
  .card--back { background: var(--orange); display: flex; align-items: center; justify-content: center; }
  .back-pattern { position: absolute; inset: 0; background: linear-gradient(135deg, var(--orange) 0%, var(--orange-light) 50%, var(--orange) 100%); }
  .back-brand {
    position: relative; display: flex; align-items: center; gap: 10px;
    font-family: "Montserrat", sans-serif; font-weight: 700; font-size: 16px; letter-spacing: .5px;
    color: var(--paper); text-transform: uppercase;
  }
  .back-brand__square { width: 26px; height: 26px; background: var(--paper); }
</style>
</head>
<body>
<main class="canvas">

  <section class="card card--front" aria-label="Business card front">
    <h1 class="holder"><span class="holder__first">CARL</span> WHITBY</h1>

    <div class="brand">
      <span class="brand__square"></span>
      <span class="brand__rule"></span>
      <span class="brand__name">Halbrook Paving<br>Works</span>
    </div>

    <p class="abn">ABN 27813046652</p>

    <ul class="contact">
      <li>
        <svg viewBox="0 0 12 12" aria-hidden="true"><path fill="#f26a22" d="M2.5 1h2l1 3-1.3 1a6 6 0 0 0 2.8 2.8L8 6.5l3 1v2a1.5 1.5 0 0 1-1.5 1.5A8.5 8.5 0 0 1 1 2.5 1.5 1.5 0 0 1 2.5 1z"/></svg>
        0418352790
      </li>
      <li>
        <svg viewBox="0 0 12 12" aria-hidden="true"><rect x="0.5" y="2" width="11" height="8" fill="#f26a22"/><path d="M1 2.6 6 6.4l5-3.8" fill="none" stroke="#fff" stroke-width="1"/></svg>
        carlwhitby@mailnest.com.au
      </li>
    </ul>

    <ul class="services">
      <li class="services__lead">For all your<br>concreting solutions</li>
      <li>Excavation</li>
      <li>Exposed &amp; colour concrete</li>
      <li>House &amp; shed slabs</li>
      <li>Driveways | Landing &amp; steps</li>
    </ul>

    <svg class="footer-bands" viewBox="0 0 540 34" aria-hidden="true">
      <polygon points="0,18 300,18 290,34 0,34" fill="#f26a22"/>
      <polygon points="322,0 540,0 540,34 300,34" fill="#5f5f5f"/>
    </svg>
  </section>

  <section class="card card--back" aria-label="Business card back">
    <div class="back-pattern" role="img" aria-label="Faint repeating diamond pattern in light orange tones"></div>
    <div class="back-brand">
      <span class="back-brand__square"></span>
      <span>Halbrook Paving Works</span>
    </div>
  </section>

</main>
</body>
</html>
```